i need a business card for a plumbing company in california

we are a drain cleaning , maintenance plumbing company who is starting new marketing campaign for a tatrench-less pipe installation department .

Target Market(s)

the professional who appreciates time and quality workmanship.

Industry/Entity Type

Plumbing

Colors
0655a3
ec1f27

Requirements
Must have
• the second logo needs to be included
Nice to have
• a focus on the services offered
Should not have
• any underlined words on the brief

```html
<!DOCTYPE html>
<html lang="en">
<head>
<meta charset="utf-8">
<title>Clearflow Plumbing – Business Card</title>
<link href="https://fonts.googleapis.com/css2?family=Open+Sans:wght@400;600;700;800&display=swap" rel="stylesheet">
<style>
  :root {
    --red: #ec1f27;
    --red-deep: #c01e26;
    --red-shade: #b81c23;
    --stone: #7f7d70;
    --white: #ffffff;
  }
  * { margin: 0; padding: 0; box-sizing: border-box; }
  html, body {
    width: 1200px;
    height: 720px;
    overflow: hidden;
    background: var(--white);
  }
  .card {
    position: relative;
    width: 1200px;
    height: 720px;
    background: var(--white);
    font-family: "Open Sans", Arial, sans-serif;
    overflow: hidden;
  }
  .card__artwork {
    position: absolute;
    left: 0;
    top: 0;
    width: 1200px;
    height: 250px;
    background: linear-gradient(90deg, var(--stone) 0%, var(--stone) 50%, var(--red-deep) 80%, var(--red) 100%);
  }

  .headline {
    position: absolute;
    left: 206px;
    width: 420px;
    text-align: center;
  }
  .headline__company {
    top: 68px;
    font-size: 47px;
    font-weight: 800;
    letter-spacing: 2px;
    color: var(--red);
  }
  .headline__service {
    top: 148px;
    font-size: 22px;
    font-weight: 400;
    letter-spacing: 4.2px;
    word-spacing: 8px;
    color: var(--white);
  }

  .contacts {
    position: absolute;
    right: 116px;
    top: 318px;
    list-style: none;
  }
  .contact {
    display: flex;
    align-items: center;
    justify-content: flex-end;
    height: 58px;
    margin-bottom: 43px;
  }
  .contact__text {
    text-align: right;
    font-size: 18px;
    font-weight: 700;
    letter-spacing: 1.6px;
    line-height: 24px;
    color: var(--red);
    margin-right: 32px;
  }
  .contact__icon {
    width: 58px;
    height: 58px;
    background: var(--red);
    display: flex;
    align-items: center;
    justify-content: center;
  }
  .contact__icon svg { width: 40px; height: 40px; }
  .icon-disc { fill: var(--red-shade); }
  .icon-glyph { fill: none; stroke: var(--white); stroke-width: 2; }
  .icon-fill { fill: var(--white); }

  .brand {
    position: absolute;
    left: 38px;
    top: 534px;
    display: flex;
    align-items: center;
    gap: 16px;
  }
  .brand__name {
    font-size: 40px;
    font-weight: 700;
    line-height: 46px;
    color: var(--stone);
  }
  .brand__mark {
    width: 52px;
    height: 52px;
    background: var(--red);
  }
</style>
</head>
<body>
<main class="card">
  <div class="card__artwork" role="img" aria-label="Decorative red and grey wave artwork"></div>

  <h1 class="headline headline__company">COMPANY</h1>
  <p class="headline headline__service">FOR DRAIN CLEANING</p>

  <ul class="contacts">
    <li class="contact">
      <p class="contact__text">+0000 0000 000<br>+2222 2222 222</p>
      <span class="contact__icon">
        <svg viewBox="0 0 40 40" aria-hidden="true">
          <circle class="icon-disc" cx="20" cy="20" r="18"/>
          <path class="icon-fill" d="M14 11c1-1 2-1 3 0l2 3c.6 1 .3 2-.5 2.6l-1 .8c.8 2 2.6 3.8 4.6 4.6l.8-1c.6-.8 1.6-1.1 2.6-.5l3 2c1 .7 1 2 0 3l-1.5 1.5c-1.2 1.2-3.5 1-6-.5-3.2-2-6-4.8-8-8-1.5-2.5-1.7-4.8-.5-6z"/>
        </svg>
      </span>
    </li>
    <li class="contact">
      <p class="contact__text">WWW.@EXAMPLE.COM</p>
      <span class="contact__icon">
        <svg viewBox="0 0 40 40" aria-hidden="true">
          <circle class="icon-disc" cx="20" cy="20" r="18"/>
          <circle class="icon-glyph" cx="20" cy="20" r="11"/>
          <ellipse class="icon-glyph" cx="20" cy="20" rx="5" ry="11"/>
          <path class="icon-glyph" d="M9 20h22M11 14h18M11 26h18"/>
        </svg>
      </span>
    </li>
    <li class="contact">
      <p class="contact__text">WWW.EXAMPLE@MAILBOX.COM</p>
      <span class="contact__icon">
        <svg viewBox="0 0 40 40" aria-hidden="true">
          <circle class="icon-disc" cx="20" cy="20" r="18"/>
          <rect class="icon-glyph" x="10" y="13" width="20" height="14"/>
          <path class="icon-glyph" d="M10 13l10 8 10-8M10 27l7-7M30 27l-7-7"/>
        </svg>
      </span>
    </li>
    <li class="contact">
      <p class="contact__text">WWW.EXAMPLE@SOCIALPAGE.COM</p>
      <span class="contact__icon">
        <svg viewBox="0 0 40 40" aria-hidden="true">
          <circle class="icon-disc" cx="20" cy="20" r="18"/>
        </svg>
      </span>
    </li>
  </ul>

  <div class="brand">
    <p class="brand__name">Clearflow<br>Plumbing</p>
    <span class="brand__mark" aria-hidden="true"></span>
  </div>
</main>
</body>
</html>
```